Boutique Recruiting Firm Needs Eye-Catching Business Cards (and potentially new logo)!

I run a recruiting company in Charleston, South Carolina. I have a ton of networking events coming up and need business cards to grab potential clients attention.

I currently have a logo but if you want to try and recreate the logo to something more modern I am open to that. If you do decide to create a new logo please submit the business card with the old logo and the new one.

Staffing Under Blue Lanterns, LLC is the name of my company. I create videos to my clients and candidates which allows me to standout from my competition so I would like a business card (and possibly new logo) to do the same.

I do not specialize in any one industry of recruiting.

```html
<!DOCTYPE html>
<html lang="en">
<head>
<meta charset="utf-8">
<title>Staffing Under Blue Lanterns — Business Card</title>
<link rel="stylesheet" href="https://fonts.googleapis.com/css2?family=Arimo:wght@400;700&family=Old+Standard+TT:wght@700&display=swap">
<style>
  :root {
    --page-bg: #d9d3cb;
    --card-top: #f1eeea;
    --card-bottom: #ddd6cf;
    --ink: #1a1a1a;
    --ink-soft: #2b2b2b;
    --band: #0d0d0d;
    --icon-glyph: #f1eeea;
  }
  * { margin: 0; padding: 0; box-sizing: border-box; }
  html, body {
    width: 1200px;
    height: 970px;
    overflow: hidden;
    background: var(--page-bg);
  }
  .canvas {
    position: relative;
    width: 1200px;
    height: 970px;
  }
  .card {
    position: absolute;
    left: 100px;
    top: 185px;
    width: 1000px;
    height: 600px;
    background: linear-gradient(180deg, var(--card-top) 0%, var(--card-bottom) 100%);
    box-shadow: 0 14px 40px rgba(0,0,0,0.18);
    overflow: hidden;
  }
  .brand {
    position: absolute;
    left: 38px;
    top: 215px;
    width: 490px;
    display: flex;
    align-items: center;
    gap: 18px;
  }
  .brand-mark {
    flex: none;
    width: 22px;
    height: 22px;
    background: var(--ink);
  }
  .brand-name {
    font-family: "Arimo", sans-serif;
    font-weight: 700;
    font-size: 40px;
    line-height: 1.15;
    color: var(--ink);
    letter-spacing: -0.5px;
  }
  .divider {
    position: absolute;
    left: 552px;
    top: 95px;
    width: 3px;
    height: 366px;
    background: var(--ink);
  }
  .person {
    position: absolute;
    left: 577px;
    top: 128px;
  }
  .person-name {
    font-family: "Old Standard TT", serif;
    font-weight: 700;
    font-size: 45px;
    line-height: 1;
    color: var(--ink);
  }
  .person-role {
    margin-top: 16px;
    font-family: "Arimo", sans-serif;
    font-size: 29px;
    line-height: 1.18;
    color: var(--ink-soft);
  }
  .contacts {
    position: absolute;
    left: 579px;
    top: 320px;
    list-style: none;
  }
  .contact {
    display: flex;
    align-items: center;
    gap: 18px;
    height: 42px;
    font-family: "Arimo", sans-serif;
    font-size: 28px;
    color: var(--ink-soft);
  }
  .contact svg { flex: none; width: 22px; height: 22px; }
  .rule {
    position: absolute;
    left: 0;
    top: 540px;
    width: 100%;
    height: 3px;
    background: var(--band);
  }
  .band {
    position: absolute;
    left: 0;
    top: 551px;
    width: 100%;
    height: 49px;
    background: var(--band);
  }
</style>
</head>
<body>
<div class="canvas">
  <div class="card">
    <div class="brand">
      <span class="brand-mark"></span>
      <span class="brand-name">Staffing Under<br>Blue Lanterns, LLC</span>
    </div>

    <div class="divider"></div>

    <div class="person">
      <div class="person-name">Marian Delacroix</div>
      <div class="person-role">Founder<br>Executive Recruiter</div>
    </div>

    <ul class="contacts">
      <li class="contact">
        <svg viewBox="0 0 22 22" aria-hidden="true">
          <rect width="22" height="22" fill="var(--ink)"/>
          <path d="M5 8 Q11 3 17 8 L15 10 L13 8.5 L9 8.5 L7 10 Z" fill="var(--icon-glyph)"/>
          <rect x="6" y="11" width="10" height="6" fill="var(--icon-glyph)"/>
        </svg>
        <span>021 5550 1934</span>
      </li>
      <li class="contact">
        <svg viewBox="0 0 22 22" aria-hidden="true">
          <rect width="22" height="22" fill="var(--ink)"/>
          <rect x="4" y="6.5" width="14" height="9.5" fill="none" stroke="var(--icon-glyph)" stroke-width="1.6"/>
          <path d="M4 6.5 L11 12 L18 6.5" fill="none" stroke="var(--icon-glyph)" stroke-width="1.6"/>
        </svg>
        <span>hello@bluelanterns.com</span>
      </li>
      <li class="contact">
        <svg viewBox="0 0 22 22" aria-hidden="true">
          <rect width="22" height="22" fill="var(--ink)"/>
          <path d="M11 18 C7 13 6.5 11 6.5 9.5 A4.5 4.5 0 0 1 15.5 9.5 C15.5 11 15 13 11 18 Z" fill="var(--icon-glyph)"/>
          <circle cx="11" cy="9.5" r="1.7" fill="var(--ink)"/>
        </svg>
        <span>42 E. Calhoun, Aiken, SC 298</span>
      </li>
    </ul>

    <div class="rule"></div>
    <div class="band"></div>
  </div>
</div>
</body>
</html>
```